Teff Flour Bags

Need simple text, and a small design, in an "Ai File" to eventually be put on a plain brown bag 20lb. I need to send the "AI File" to a company, and they will do the printing onthe bags.

"TEFF FLOUR BROWN" please see uploaded file for samples

```html
<!DOCTYPE html>
<html lang="en">
<head>
<meta charset="UTF-8">
<title>Teff Flour Brown – Bag Label</title>
<link href="https://fonts.googleapis.com/css2?family=Source+Serif+4:wght@400;600&display=swap" rel="stylesheet">
<style>
  :root {
    --kraft: #c9a57a;
    --kraft-light: #d4b28a;
    --ink: #141110;
    --ink-soft: #2a2320;
    --art-top: #3a302a;
    --art-bottom: #1e1916;
  }
  * { margin: 0; padding: 0; box-sizing: border-box; }
  html, body { width: 1200px; height: 800px; overflow: hidden; }
  body {
    background: radial-gradient(ellipse at 50% 40%, var(--kraft-light), var(--kraft));
    color: var(--ink);
    font-family: "Source Serif 4", Georgia, serif;
  }
  .label {
    width: 1200px;
    height: 800px;
    display: flex;
    flex-direction: column;
    align-items: center;
  }
  .illustration {
    margin-top: 52px;
    width: 236px;
    height: 292px;
    border-radius: 6px;
    background: linear-gradient(180deg, var(--art-top), var(--art-bottom));
  }
  .established {
    margin-top: 30px;
    font-size: 19px;
    letter-spacing: 1.5px;
    color: var(--ink-soft);
  }
  .product-name {
    margin-top: 10px;
    font-size: 92px;
    font-weight: 600;
    line-height: 1;
    letter-spacing: 2px;
  }
  .variant {
    margin-top: 24px;
    width: 300px;
    height: 62px;
    display: flex;
    align-items: center;
    justify-content: center;
    background: var(--ink);
    color: var(--kraft-light);
    font-size: 36px;
    font-weight: 600;
    letter-spacing: 2px;
  }
  .net-weight {
    margin-top: 30px;
    font-size: 21px;
    font-weight: 600;
    letter-spacing: 0.5px;
  }
</style>
</head>
<body>
  <main class="label">
    <div class="illustration" role="img" aria-label="Illustration area: windmill on a hill with a winding path and sun rays"></div>
    <p class="established">ESTABLISHED 2019</p>
    <h1 class="product-name">TEFF FLOUR</h1>
    <p class="variant">BROWN</p>
    <p class="net-weight">Net Weight 20 LBS. ( 9.07kg)</p>
  </main>
</body>
</html>
```